Flyer Design for Norvane LLC

We need a Flyer for a new company called “Norvane LLC”. This is a technology process improvement company providing a comprehensive assessment of the technology used to run their business. The documentation and review process delivers the visibility and reassurance they need to protect their business and plan for the future. The product is called “Systems Pathcharting”. Our primary target is small-medium size businesses, with the deliverables going to the decision maker.

We would like to see the designs use the color blue. Our tag line is "Protect Your Business · Take Control of IT".

- Attached: Norvane LLC Overview document we put together as a starting point. Use as much or as little as you wish.
- Attached: Business Card and Logo designs for colors, etc.

Industry/Entity Type

It Company

```html
<!DOCTYPE html>
<html lang="en">
<head>
<meta charset="utf-8">
<title>Norvane LLC Flyer</title>
<link href="https://fonts.googleapis.com/css2?family=Source+Sans+3:wght@400;600;700&display=swap" rel="stylesheet">
<style>
  :root {
    --brand-blue: #0b72bd;
    --deep-blue: #0a63a6;
    --charcoal: #3a3a3c;
    --band-dark: rgba(38,38,40,0.92);
    --band-mid: rgba(50,50,52,0.78);
    --text-grey: #4a4a4a;
    --paper: #ffffff;
  }
  * { box-sizing: border-box; margin: 0; padding: 0; }
  html, body { width: 1008px; height: 1200px; overflow: hidden; background: var(--paper); }
  body { font-family: "Source Sans 3", sans-serif; color: var(--text-grey); }
  .flyer { position: relative; width: 1008px; height: 1200px; background: var(--paper); }

  .hero-photo {
    position: absolute; left: 0; top: 150px; width: 964px; height: 518px;
    background: linear-gradient(160deg, #e9ebec 0%, #c9cdd0 35%, #8f9599 65%, #5b6064 100%);
    border-bottom-right-radius: 70px; overflow: hidden;
  }
  .hero-band {
    position: absolute; left: 0; bottom: 0; width: 100%; height: 102px;
    text-align: center; color: #fff;
  }
  .hero-band .band-head {
    height: 45px; background: var(--band-mid);
    font-size: 24px; font-weight: 600; line-height: 48px;
  }
  .hero-band .band-body {
    height: 57px; background: var(--band-dark);
    font-size: 18px; line-height: 22px; padding-top: 6px;
  }

  .tagline-box {
    position: absolute; left: 33px; top: 0; width: 253px; height: 260px;
    background: var(--brand-blue); color: #fff; text-align: center;
    font-size: 26px; font-weight: 600; line-height: 36px; padding-top: 112px;
  }

  .brand {
    position: absolute; left: 725px; top: 40px; width: 229px; height: 90px;
    display: flex; align-items: center; justify-content: center; gap: 10px;
  }
  .brand-mark { width: 22px; height: 22px; background: var(--brand-blue); }
  .brand-name { font-size: 32px; font-weight: 700; color: var(--brand-blue); }

  .help { position: absolute; left: 36px; top: 716px; width: 452px; }
  .help h2 { font-size: 21px; font-weight: 700; color: var(--brand-blue); margin-bottom: 6px; }
  .help p { font-size: 15px; line-height: 18px; text-align: justify; margin-bottom: 18px; }
  .help h3 { font-size: 17px; font-weight: 600; color: var(--brand-blue); margin-top: 12px; margin-bottom: 12px; }
  .areas { list-style: none; display: grid; grid-template-columns: 213px 200px; row-gap: 3px; font-size: 16px; }
  .areas li { display: flex; align-items: center; gap: 6px; }
  .dot { width: 11px; height: 11px; flex: none; }

  .deliverables {
    position: absolute; left: 571px; top: 727px; width: 393px; height: 330px;
    background: var(--brand-blue); border-bottom-left-radius: 10px; border-bottom-right-radius: 10px;
    color: #fff;
  }
  .deliverables h2 {
    height: 58px; background: var(--charcoal); font-size: 21px; font-weight: 600;
    line-height: 62px; padding-left: 25px;
  }
  .deliverables ul { list-style: none; padding: 19px 0 0 25px; }
  .deliverables li { display: flex; align-items: center; gap: 12px; font-size: 19px; height: 27px; }
  .deliverables .dot { width: 14px; height: 14px; }

  .cta {
    position: absolute; left: 47px; top: 1098px; width: 915px; height: 50px;
    background: var(--brand-blue); border-radius: 25px; color: #fff;
    display: flex; align-items: center; justify-content: center; gap: 14px;
    font-size: 25px; font-weight: 600;
  }
  .cta .phone { display: flex; align-items: center; gap: 12px; margin-left: 4px; }
  .contact {
    position: absolute; left: 0; top: 1156px; width: 100%; text-align: center;
    font-size: 19px; letter-spacing: 0.6px; color: #555;
  }
  .contact .sep { margin: 0 10px; }
</style>
</head>
<body>
<div class="flyer">

  <div class="hero-photo" role="img" aria-label="Photo of a business team meeting in a bright glass-walled conference room">
    <div class="hero-band">
      <div class="band-head">YOU HAVE BIG PLANS, RIGHT?</div>
      <div class="band-body">Technology may help you get there, but how can you plan where you want to go<br>without defining where you are today?</div>
    </div>
  </div>

  <div class="tagline-box">PROTECT<br>YOUR BUSINESS<br>TAKE CONTROL<br>OF IT</div>

  <div class="brand">
    <span class="brand-mark"></span>
    <span class="brand-name">Norvane LLC</span>
  </div>

  <section class="help">
    <h2>WE CAN HELP!</h2>
    <p>Norvane LLC provides a comprehensive assessment of the technology used to run your business. The documentation and review process delivers the visibility and reassurance you need to protect your business.</p>
    <p>Our team understands that each business operates on its own unique complexities, and crafting a solution requires a custom, unbiased review. Positioning your company with the right insight is intrumental to your success and our goal as your technology partner.</p>
    <h3>EVALUATING FIVE FUNCTIONAL AREAS</h3>
    <ul class="areas">
      <li><svg class="dot" viewBox="0 0 12 12"><circle cx="6" cy="6" r="6" fill="#0b72bd"/><path d="M4.8 3.5 7.3 6 4.8 8.5" stroke="#fff" stroke-width="1.6" fill="none"/></svg>It Service Delivery</li>
      <li><svg class="dot" viewBox="0 0 12 12"><circle cx="6" cy="6" r="6" fill="#0b72bd"/><path d="M4.8 3.5 7.3 6 4.8 8.5" stroke="#fff" stroke-width="1.6" fill="none"/></svg>Planning</li>
      <li><svg class="dot" viewBox="0 0 12 12"><circle cx="6" cy="6" r="6" fill="#0b72bd"/><path d="M4.8 3.5 7.3 6 4.8 8.5" stroke="#fff" stroke-width="1.6" fill="none"/></svg>Infrastructure Services</li>
      <li><svg class="dot" viewBox="0 0 12 12"><circle cx="6" cy="6" r="6" fill="#0b72bd"/><path d="M4.8 3.5 7.3 6 4.8 8.5" stroke="#fff" stroke-width="1.6" fill="none"/></svg>IT Administration</li>
      <li><svg class="dot" viewBox="0 0 12 12"><circle cx="6" cy="6" r="6" fill="#0b72bd"/><path d="M4.8 3.5 7.3 6 4.8 8.5" stroke="#fff" stroke-width="1.6" fill="none"/></svg>Application Services</li>
    </ul>
  </section>

  <section class="deliverables">
    <h2>DOSSIER DELIVERABLES</h2>
    <ul>
      <li><svg class="dot" viewBox="0 0 12 12"><circle cx="6" cy="6" r="6" fill="#fff"/><path d="M4.8 3.5 7.3 6 4.8 8.5" stroke="#0b72bd" stroke-width="1.6" fill="none"/></svg>Executive Dashboard</li>
      <li><svg class="dot" viewBox="0 0 12 12"><circle cx="6" cy="6" r="6" fill="#fff"/><path d="M4.8 3.5 7.3 6 4.8 8.5" stroke="#0b72bd" stroke-width="1.6" fill="none"/></svg>Technology Product Summary</li>
      <li><svg class="dot" viewBox="0 0 12 12"><circle cx="6" cy="6" r="6" fill="#fff"/><path d="M4.8 3.5 7.3 6 4.8 8.5" stroke="#0b72bd" stroke-width="1.6" fill="none"/></svg>Recommended IT Policies</li>
      <li><svg class="dot" viewBox="0 0 12 12"><circle cx="6" cy="6" r="6" fill="#fff"/><path d="M4.8 3.5 7.3 6 4.8 8.5" stroke="#0b72bd" stroke-width="1.6" fill="none"/></svg>Potential Cost Savings</li>
      <li><svg class="dot" viewBox="0 0 12 12"><circle cx="6" cy="6" r="6" fill="#fff"/><path d="M4.8 3.5 7.3 6 4.8 8.5" stroke="#0b72bd" stroke-width="1.6" fill="none"/></svg>Technology&nbsp; Recommendations</li>
      <li><svg class="dot" viewBox="0 0 12 12"><circle cx="6" cy="6" r="6" fill="#fff"/><path d="M4.8 3.5 7.3 6 4.8 8.5" stroke="#0b72bd" stroke-width="1.6" fill="none"/></svg>In-depth Questionnaire</li>
      <li><svg class="dot" viewBox="0 0 12 12"><circle cx="6" cy="6" r="6" fill="#fff"/><path d="M4.8 3.5 7.3 6 4.8 8.5" stroke="#0b72bd" stroke-width="1.6" fill="none"/></svg>Technology Product Details</li>
      <li><svg class="dot" viewBox="0 0 12 12"><circle cx="6" cy="6" r="6" fill="#fff"/><path d="M4.8 3.5 7.3 6 4.8 8.5" stroke="#0b72bd" stroke-width="1.6" fill="none"/></svg>Full Infrastructure Detailed Report</li>
    </ul>
  </section>

  <div class="cta">
    <span>TAKE THE FIRST STEP - CALL US TODAY!</span>
    <span class="phone">
      <svg width="22" height="22" viewBox="0 0 24 24" aria-hidden="true">
        <circle cx="12" cy="12" r="10.5" fill="none" stroke="#fff" stroke-width="2"/>
        <path d="M8.6 6.8c.4-.3.9-.2 1.1.2l1 1.9c.2.4.1.8-.2 1.1l-.6.5c.5 1.2 1.4 2.2 2.6 2.8l.5-.6c.3-.3.8-.4 1.1-.2l1.9 1c.4.2.5.7.2 1.1l-.7.9c-.4.5-1.1.7-1.7.5-2.8-1-5-3.2-6-6-.2-.6 0-1.3.5-1.7z" fill="#fff"/>
      </svg>
      866-555-0142
    </span>
  </div>

  <div class="contact">sales@norvanellc.com<span class="sep">|</span>www.norvanellc.com</div>
</div>
</body>
</html>
```